Velvet Orchid Beauty Bar Business Card

We need a modern, elegant business card design for our new beauty bar located in La Quinta, CA. The card should feel premium yet approachable, reflecting our brand identity: warm, stylish, and confidence-boosting.

Use our existing Velvet Orchid Beauty Bar logo (to be provided as vector file).

Colors: Black, White, Blush / Nude accents, and Gold (metallic or foil effect if possible).

Typography: Clean sans-serif for clarity, with optional elegant script accent.
Design Style

Minimalist and modern with plenty of white space.

Premium look with a beauty/lifestyle feel (not overly corporate).

Option to explore vertical or horizontal orientation.

Rounded corners welcome, but not required.

Additional Notes

Design should print well in both matte and glossy finishes.

Please present mockups with both light and dark backgrounds.

Keep overall feel sleek, feminine, and high-end while still being approachable.

```html
<!DOCTYPE html>
<html lang="en">
<head>
<meta charset="utf-8">
<title>Velvet Orchid Beauty Bar — Business Card</title>
<link href="https://fonts.googleapis.com/css2?family=Poppins:wght@400;500;600&display=swap" rel="stylesheet">
<style>
  :root {
    --stage: #2a292d;
    --card: #1f1f21;
    --card-edge: #2c2c2f;
    --art-deep: #0e0e10;
    --art-mid: #17171a;
    --silver: #dcdcde;
    --white: #f4f4f4;
    --blush: #e6c2b4;
    --gold: #c9a66b;
    --gold-light: #e3c98f;
  }
  * { margin: 0; padding: 0; box-sizing: border-box; }
  html, body { width: 1200px; height: 800px; overflow: hidden; background: var(--stage); }
  body { font-family: "Poppins", sans-serif; }

  .canvas {
    position: relative;
    width: 1200px; height: 800px;
    display: flex; align-items: center; justify-content: center; gap: 40px;
  }

  .card {
    position: relative;
    width: 540px; height: 310px;
    background: var(--card);
    border-radius: 22px;
    border: 1px solid var(--card-edge);
    overflow: hidden;
  }

  /* Front */
  .front-art {
    position: absolute; left: -60px; top: 30px;
    width: 330px; height: 330px;
    border-radius: 50% 50% 0 50%;
    background:
      radial-gradient(circle at 60% 45%, var(--art-mid) 0%, var(--art-deep) 70%);
    box-shadow: inset -1px -1px 0 rgba(201,166,107,.35);
  }
  .front-brand {
    position: absolute; right: 44px; top: 50%;
    transform: translateY(-50%);
    text-align: center;
    color: var(--silver);
  }

  .brand-name {
    font-weight: 500;
    font-size: 26px;
    letter-spacing: 0.05em;
    text-transform: uppercase;
    line-height: 1.15;
    white-space: nowrap;
  }
  .brand-sub {
    display: flex; align-items: center; gap: 10px;
    margin-top: 8px;
    font-size: 13px; font-weight: 400;
    letter-spacing: 0.03em;
    white-space: nowrap;
  }
  .brand-sub::before, .brand-sub::after {
    content: ""; flex: 1; height: 1px; min-width: 20px;
    background: linear-gradient(90deg, var(--gold), var(--gold-light));
  }

  /* Back */
  .back-brand {
    position: absolute; left: 30px; top: 50%;
    transform: translateY(-50%);
    width: 232px;
    text-align: center;
    color: var(--white);
  }
  .back-divider {
    position: absolute; left: 284px; top: 70px;
    width: 1px; height: 170px;
    background: linear-gradient(180deg, transparent, var(--gold) 20%, var(--gold) 80%, transparent);
  }
  .contact {
    position: absolute; left: 306px; top: 74px;
    color: var(--white);
  }
  .contact-name { font-weight: 600; font-size: 18px; letter-spacing: 0.03em; line-height: 1.3; }
  .contact-role { font-size: 11px; color: var(--blush); letter-spacing: .08em; margin-bottom: 14px; }
  .contact-address { font-size: 12px; line-height: 1.55; margin-bottom: 12px; }
  .contact-line { display: flex; align-items: center; gap: 8px; font-size: 12px; line-height: 1.9; }
  .contact-line svg { width: 12px; height: 12px; fill: var(--gold-light); flex: none; }
</style>
</head>
<body>
<main class="canvas">

  <section class="card card-front" aria-label="Card front">
    <div class="front-art" role="img" aria-label="Large embossed gloss-black line-art profile illustration"></div>
    <div class="front-brand">
      <div class="brand-name">Velvet Orchid</div>
      <div class="brand-sub">Beauty Bar by Marisol</div>
    </div>
  </section>

  <section class="card card-back" aria-label="Card back">
    <div class="back-brand">
      <div class="brand-name">Velvet Orchid</div>
      <div class="brand-sub">Beauty Bar by Marisol</div>
    </div>
    <div class="back-divider"></div>
    <div class="contact">
      <p class="contact-name">LENA R COLE</p>
      <p class="contact-role">CEO</p>
      <p class="contact-address">PO BOX 48 Calle Tampico<br>La Quinta, CA 92253</p>
      <p class="contact-line">
        <svg viewBox="0 0 24 24" aria-hidden="true"><path d="M6.6 10.8a15.1 15.1 0 0 0 6.6 6.6l2.2-2.2a1 1 0 0 1 1-.25 11.4 11.4 0 0 0 3.6.57 1 1 0 0 1 1 1V20a1 1 0 0 1-1 1A17 17 0 0 1 3 4a1 1 0 0 1 1-1h3.5a1 1 0 0 1 1 1c0 1.25.2 2.46.57 3.6a1 1 0 0 1-.25 1z"/></svg>
        (555) 014-2287
      </p>
      <p class="contact-line">
        <svg viewBox="0 0 24 24" aria-hidden="true"><path d="M2 5h20v14H2z M4 7v.4l8 5 8-5V7l-8 5z" fill-rule="evenodd"/></svg>
        hello@velvetorchid.co
      </p>
    </div>
  </section>

</main>
</body>
</html>
```